Web Design

QLV Institute offers a one stop solution for people to be introduced to the world of Forex trading. We have interactive forex room, one on one coaching by our experienced trading experts.
Main menus:
1. Learn to trade
2. About us
3. Brokers
4. Money management and risk
5. FAQ
6. Register – scroll down menu with registration form (name, email and register button)
7. Contact us
The webpage should have:
1. Large text style and images
2. Join / Get Started Buttons
3. Instructors profile
4. People Testimonies
5. Recommended Brokers
6. Live rates
7. Live support
8. Social icons: facebook, twitter and g+

Project Deadline Extended
Reason: I just added a logo on the attachment

Industry/Entity Type

Trade

```html
<!DOCTYPE html>
<html lang="en">
<head>
<meta charset="utf-8">
<title>QLV Institute – What We Do</title>
<link rel="stylesheet" href="https://fonts.googleapis.com/css2?family=Montserrat:wght@600;700&family=Figtree:wght@400&family=Lato:ital,wght@1,400&display=swap">
<style>
  :root {
    --page-bg: #ffffff;
    --ink: #111111;
    --accent-purple: #9b59b6;
    --button-purple: #a264b8;
    --button-border: #8e52a3;
    --panel-teal: #00b99b;
    --field-bg: #f1f1f1;
    --field-border: #cfcfcf;
    --placeholder: #b9b9b9;
    --hero-light: #e9eaee;
    --hero-dark: #3a3d44;
    --office-light: #f2f2cf;
    --office-dark: #1c2440;
  }
  * { box-sizing: border-box; }
  html, body {
    margin: 0;
    width: 1200px;
    height: 696px;
    overflow: hidden;
    background: var(--page-bg);
  }
  .page {
    position: relative;
    width: 1200px;
    height: 696px;
    overflow: hidden;
    font-family: "Figtree", "Helvetica Neue", Arial, sans-serif;
    color: var(--ink);
  }
  .hero-photo {
    position: absolute;
    left: 75px;
    top: 0;
    width: 1024px;
    height: 142px;
    background: linear-gradient(90deg, var(--hero-dark) 0%, #5a5e68 28%, #cfd1d6 48%, var(--hero-light) 62%, #f2f3f5 100%);
  }
  .about {
    position: absolute;
    left: 150px;
    top: 210px;
    width: 592px;
  }
  .about__title {
    margin: 0;
    padding-bottom: 2px;
    font-family: "Montserrat", "Helvetica Neue", Arial, sans-serif;
    font-weight: 700;
    font-size: 21px;
    letter-spacing: 0.2px;
    line-height: 25px;
    border-bottom: 2px solid var(--accent-purple);
  }
  .about__text {
    margin: 16px 0 0;
    font-size: 12.6px;
    line-height: 19.7px;
    white-space: nowrap;
  }
  .about__text + .about__text { margin-top: 19.7px; }
  .signup {
    position: absolute;
    left: 769px;
    top: 207px;
    width: 281px;
    height: 345px;
    background: var(--panel-teal);
  }
  .signup__field {
    position: absolute;
    left: 22px;
    width: 237px;
    height: 31px;
    padding: 0 7px;
    border: 1px solid var(--field-border);
    background: var(--field-bg);
    font-family: "Lato", Arial, sans-serif;
    font-style: italic;
    font-size: 13px;
    color: var(--ink);
    outline: none;
  }
  .signup__field::placeholder { color: var(--placeholder); }
  .signup__field--name { top: 49px; }
  .signup__field--surname { top: 103px; }
  .signup__field--email { top: 157px; }
  .signup__field--nationality { top: 211px; }
  .signup__button {
    position: absolute;
    left: 80px;
    top: 276px;
    width: 123px;
    height: 31px;
    border: 1px solid var(--button-border);
    background: var(--button-purple);
    color: #ffffff;
    font-family: "Montserrat", "Helvetica Neue", Arial, sans-serif;
    font-weight: 600;
    font-size: 15px;
    cursor: pointer;
  }
  .feature-photo {
    position: absolute;
    top: 621px;
    width: 281px;
    height: 75px;
    background: linear-gradient(180deg, var(--office-light) 0%, #e9ebc9 45%, #6f7488 75%, var(--office-dark) 100%);
  }
  .feature-photo--one { left: 150px; }
  .feature-photo--two { left: 459px; }
  .feature-photo--three { left: 769px; }
</style>
</head>
<body>
<div class="page">
  <div class="hero-photo" role="img" aria-label="Businessman in a suit pointing a pen at a trading chart on a whiteboard"></div>

  <section class="about">
    <h2 class="about__title">WHAT WE DO</h2>
    <p class="about__text">QLV Institute offers a one stop solution for people who want to be introduced to the world of Forex<br>trading. Whether you are a complete beginner or an active trader looking to sharpen your skills, our<br>programme walks you through every step, from reading currency pairs and charts to placing your first<br>trade with confidence. Our interactive forex room lets you watch live markets alongside our team and<br>ask questions as prices move. You can also book one on one coaching sessions with our experienced<br>trading experts, who will review your strategy, help you build a trading plan and show you how to<br>manage money and risk. Every course is built around real market conditions, so what you learn can be<br>used today.</p>
    <p class="about__text">When you join, you get access to live rates, recommended brokers and a library of lessons you can<br>revisit at any time. Our live support team is on hand to answer questions about your account, the<br>platform or the markets themselves. Members also share their progress in the community, and many of<br>our instructors started out as students in this very room. Fill in the form to get started and take<br>your first step today.</p>
  </section>

  <form class="signup" action="#">
    <input class="signup__field signup__field--name" type="text" placeholder="Enter Name" aria-label="Name">
    <input class="signup__field signup__field--surname" type="text" placeholder="Enter Sirname" aria-label="Surname">
    <input class="signup__field signup__field--email" type="email" placeholder="Enter Email" aria-label="Email">
    <input class="signup__field signup__field--nationality" type="text" placeholder="Enter Nationality" aria-label="Nationality">
    <button class="signup__button" type="button">Get Started</button>
  </form>

  <div class="feature-photo feature-photo--one" role="img" aria-label="Silhouettes of traders in a bright office with tall windows"></div>
  <div class="feature-photo feature-photo--two" role="img" aria-label="Silhouettes of traders in a bright office with tall windows"></div>
  <div class="feature-photo feature-photo--three" role="img" aria-label="Silhouettes of traders in a bright office with tall windows"></div>
</div>
</body>
</html>
```